SilverLedgerOak - Double Sided Business Card

We are looking for design options or our business cards. We are a Business Solutions and HR solutions Provider - the theme is business, for this card.

Our brand colours are represented within our logo.

Details needed to be put on the front of the business card are:

Employees name: [Sample Name]
Role: [Sample Role]

Address: Suite 4 - Level 3/48 Halloran Avenue Brindlemere NSW 2163
M: 0000 000 000
P: 1300 847 213
F: 1300 847 286
E: sample@silverledgeroak.com.au
www.silverledgeroak.com.au
Updates

Reason: Hello, could we please increase our deadline by 5 days. Thanking you, Tess

Target Market(s)

Business Owners, also Candidates looking for Employment

Industry/Entity Type

Business

Contact Information for Business Card

Role: [Sample Role]

M: 0000 000 000
P: 1300 847 213
F: 1300 847 286

Font styles to use
Sans Serif

Colors
3276b5
3176b5
0455a3
85abd2
cfdeed
ffffff
000000
1b1b1b
757575

Requirements
Must have
• Details needed to be put on the front of the business card are:
• Employees name: [Sample Name]
• Role: [Sample Role]
• Address: Suite 4 - Level 3/48 Halloran Avenue Brindlemere NSW 2163
• M: 0000 000 000
• P: 1300 847 213
• F: 1300 847 286
• E: sample@silverledgeroak.com.au
• www.silverledgeroak.com.au
Nice to have
• Simplicity, clean and professional.

```html
<!DOCTYPE html>
<html lang="en">
<head>
<meta charset="utf-8">
<title>SilverLedgerOak Business Card</title>
<link rel="stylesheet" href="https://fonts.googleapis.com/css2?family=Open+Sans:wght@400;600;700&display=swap">
<style>
  :root {
    --navy: #0f2547;
    --brand-blue: #0455a3;
    --accent-blue: #3276b5;
    --light-blue: #85abd2;
    --paper: #f4f5f7;
    --white: #ffffff;
    --ink: #1b1b1b;
    --muted: #757575;
    --backdrop: #8a8c8f;
  }
  * { box-sizing: border-box; margin: 0; padding: 0; }
  html, body {
    width: 1200px; height: 904px; overflow: hidden;
    background: var(--backdrop);
    font-family: "Open Sans", Arial, sans-serif;
  }
  .canvas { position: relative; width: 1200px; height: 904px; }
  .card {
    position: absolute; width: 640px; height: 366px;
    box-shadow: 0 6px 18px rgba(0,0,0,.35);
    overflow: hidden;
  }
  /* Back side */
  .card-back { left: 100px; top: 60px; background: var(--navy); }
  .back-brand {
    position: absolute; left: 0; right: 0; top: 120px;
    display: flex; align-items: center; justify-content: center; gap: 12px;
    color: var(--white); font-weight: 600; font-size: 30px;
  }
  .brand-square { width: 22px; height: 22px; background: currentColor; }
  .back-url {
    position: absolute; left: 0; right: 0; bottom: 44px; text-align: center;
    color: var(--white); font-size: 14px; letter-spacing: 4px; opacity: .9;
  }
  /* Front side */
  .card-front { left: 460px; top: 478px; background: var(--navy); }
  .front-brand-panel {
    position: absolute; left: 0; top: 0; bottom: 0; width: 290px;
    background: var(--paper);
    display: flex; flex-direction: column; align-items: center; justify-content: center;
    padding-top: 40px;
  }
  .front-brand {
    display: flex; align-items: center; gap: 8px;
    color: var(--brand-blue); font-weight: 700; font-size: 26px;
  }
  .front-brand .brand-square { width: 18px; height: 18px; }
  .brand-rule { width: 240px; height: 1px; background: var(--muted); margin: 8px 0 5px; }
  .tagline { font-size: 9px; font-weight: 700; color: var(--ink); white-space: nowrap; }
  .divider {
    position: absolute; left: 296px; top: 0; bottom: 0; width: 3px;
    background: var(--accent-blue);
  }
  .details {
    position: absolute; left: 335px; top: 30px; color: var(--white);
  }
  .person-name { font-size: 19px; font-weight: 700; }
  .person-role { font-size: 13px; margin: 1px 0 12px 20px; color: #dfe7f1; }
  .address { font-size: 14px; line-height: 1.35; margin-left: 20px; margin-bottom: 16px; }
  .contact-list { list-style: none; margin-left: 40px; font-size: 14px; line-height: 1.4; }
  .contact-list li { display: flex; align-items: center; gap: 10px; }
  .contact-list svg { width: 13px; height: 13px; fill: none; stroke: var(--white); stroke-width: 1.5; flex: none; }
</style>
</head>
<body>
<div class="canvas">
  <section class="card card-back">
    <div class="back-brand"><span class="brand-square"></span>SilverLedgerOak</div>
    <div class="back-url">www.silverledgeroak.com.au</div>
  </section>

  <section class="card card-front">
    <div class="front-brand-panel">
      <div class="front-brand"><span class="brand-square"></span>SilverLedgerOak</div>
      <div class="brand-rule"></div>
      <div class="tagline">Guiding growing local firms toward their strongest future</div>
    </div>
    <div class="divider"></div>
    <div class="details">
      <div class="person-name">Daniel Reeve</div>
      <div class="person-role">Manager</div>
      <div class="address">Suite 4 - Level 3/48<br>Halloran Avenue<br>Brindlemere NSW 2163</div>
      <ul class="contact-list">
        <li><svg viewBox="0 0 14 14"><rect x="3.5" y="1" width="7" height="12" rx="1"/></svg>0000 000 000</li>
        <li><svg viewBox="0 0 14 14"><path d="M3 1.5l2.5 2.5-1.5 1.5c1 2 2.5 3.5 4.5 4.5l1.5-1.5 2.5 2.5-2 2C6 12.5 1.5 8 1 3.5z"/></svg>1300 847 213</li>
        <li><svg viewBox="0 0 14 14"><rect x="1" y="5" width="12" height="7"/><rect x="3.5" y="1.5" width="7" height="3.5"/></svg>1300 847 286</li>
        <li><svg viewBox="0 0 14 14"><rect x="1" y="3" width="12" height="8"/><path d="M1 3l6 5 6-5"/></svg>sample@silverledgeroak.com.au</li>
        <li><svg viewBox="0 0 14 14"><circle cx="7" cy="7" r="6"/><path d="M1 7h12M7 1c-3 3.5-3 8.5 0 12M7 1c3 3.5 3 8.5 0 12"/></svg>www.silverledgeroak.com.au</li>
      </ul>
    </div>
  </section>
</div>
</body>
</html>
```